Pacelight Arena is a web based program in the sports industry. We are looking for a modern, cutting edge business card design. We are looking for a dark base and need to use three logo's on the card. Pacelight Arena, Ferrovane Sports Supplements, and Tallow Ridge Golf Academy.
Updates

This project is guaranteed. Not sure how to do that....

Industry/Entity Type

Business

Requirements
Must have
• 3 logo's... Pacelight Arena... Tallow Ridge Golf Academy... FerroVane Sports Supplements

```html
<!DOCTYPE html>
<html lang="en">
<head>
<meta charset="utf-8">
<title>Pacelight Arena – Business Card</title>
<link href="https://fonts.googleapis.com/css2?family=Open+Sans:wght@600;700&display=swap" rel="stylesheet">
<style>
  :root {
    --page: #ffffff;
    --frame: #000000;
    --card-dark: #050505;
    --card-mid: #5c5c5c;
    --card-light: #a8a8a8;
    --brand-mark: #2e2e2e;
    --brand-warm: #c27c64;
    --partner-red: #e8203a;
    --partner-ink: #ffffff;
    --golf-ink: #111111;
    --golf-ring: #6d1f2a;
    --small-warm: #8a3a22;
  }
  * { margin: 0; padding: 0; box-sizing: border-box; }
  html, body { width: 1200px; height: 554px; overflow: hidden; background: var(--page); }
  .canvas {
    position: relative; width: 1200px; height: 554px;
    border: 3px solid var(--frame); background: var(--page);
    font-family: "Open Sans", Arial, sans-serif;
  }
  .card {
    position: absolute; left: 245px; top: 77px; width: 720px; height: 409px;
    background: linear-gradient(225deg, var(--card-light) 0%, var(--card-mid) 50%, var(--card-dark) 100%);
  }
  .brand-main {
    position: absolute; left: 98px; top: 34px; width: 600px;
    display: flex; align-items: flex-start; gap: 18px;
  }
  .brand-main__mark {
    width: 46px; height: 46px; margin-top: 40px;
    border-radius: 50%; background: var(--brand-mark); flex: none;
  }
  .brand-main__name {
    font-weight: 700; font-size: 102px; line-height: 1.0; color: var(--brand-warm);
    letter-spacing: -1px;
  }
  .partner-row {
    position: absolute; left: 0; right: 0; top: 300px; height: 100px;
  }
  .partner-supplements {
    position: absolute; left: 38px; top: 0; width: 170px; height: 100px;
    display: flex; align-items: center; gap: 10px;
  }
  .partner-supplements__mark { width: 24px; height: 24px; background: var(--partner-red); flex: none; }
  .partner-supplements__name {
    font-weight: 700; font-size: 16px; line-height: 1.2; color: var(--partner-ink);
  }
  .partner-golf {
    position: absolute; left: 296px; top: 0; width: 170px; height: 100px;
    display: flex; align-items: center; justify-content: center; gap: 8px;
  }
  .partner-golf__mark { width: 18px; height: 18px; border-radius: 50%; border: 2px solid var(--golf-ring); flex: none; }
  .partner-golf__name {
    font-weight: 700; font-size: 17px; line-height: 1.2; color: var(--golf-ink);
  }
  .brand-small {
    position: absolute; left: 540px; top: 0; width: 170px; height: 100px;
    display: flex; align-items: center; gap: 8px;
  }
  .brand-small__mark { width: 16px; height: 16px; background: var(--small-warm); flex: none; }
  .brand-small__name {
    font-weight: 700; font-size: 26px; line-height: 1.05; color: var(--small-warm);
  }
</style>
</head>
<body>
<div class="canvas">
  <div class="card">
    <div class="brand-main">
      <span class="brand-main__mark"></span>
      <span class="brand-main__name">Pacelight<br>Arena</span>
    </div>
    <div class="partner-row">
      <div class="partner-supplements">
        <span class="partner-supplements__mark"></span>
        <span class="partner-supplements__name">FerroVane Sports Supplements</span>
      </div>
      <div class="partner-golf">
        <span class="partner-golf__mark"></span>
        <span class="partner-golf__name">Tallow Ridge<br>Golf Academy</span>
      </div>
      <div class="brand-small">
        <span class="brand-small__mark"></span>
        <span class="brand-small__name">Pacelight<br>Arena</span>
      </div>
    </div>
  </div>
</div>
</body>
</html>
```